real esate business card with company logo and name

we need a business card design for a real esate company

The company name is Walsh & Brody Pty Ltd, and we have our logo designed and will upload. We want classic or moden feel. Black or white background. looks more textured. Should include folowinginformations
Paul Walsh and Lucy Brody
Sales Agents & Onsite Manager
p: 07 5948 2063
F: 07 5948 2174
M:0461 857 239
3/42 Marlin Crescent, ASHFORD VALE QLD 4190

We want this business card looks professonal. Thank you in advance.

Industry/Entity Type

Real Estate Agent

Contact Information for Business Card

Paul Walsh and Lucy Brody
Onsite Manager & Sales Agents
p: 07 5948 2063
M:0461 857 239

Font styles to use
Serif

Colors
000000
fbfbfb
333333
959595

Requirements
Must have
• company logo and name, black or white back ground

```html
<!DOCTYPE html>
<html lang="en">
<head>
<meta charset="utf-8">
<title>Walsh &amp; Brody Pty Ltd — Business Card</title>
<link rel="stylesheet" href="https://fonts.googleapis.com/css2?family=Cinzel:wght@400;600&display=swap">
<style>
  :root {
    --card-black: #000000;
    --card-charcoal: #1a1a1a;
    --ink-light: #fbfbfb;
    --ink-mid: #959595;
    --ink-dark: #333333;
    --stage: #d9d6d2;
  }
  * { margin: 0; padding: 0; box-sizing: border-box; }
  html, body {
    width: 1200px; height: 913px; overflow: hidden;
    background: var(--stage);
  }
  .stage {
    position: relative; width: 1200px; height: 913px;
    font-family: "Cinzel", "Times New Roman", serif;
  }
  .card {
    position: absolute; width: 540px; height: 330px;
    border-radius: 4px;
    background: radial-gradient(ellipse at 35% 30%, var(--card-charcoal) 0%, var(--card-black) 75%);
    box-shadow: 0 18px 36px rgba(0,0,0,.35);
    color: var(--ink-light);
    display: flex; flex-direction: column; align-items: center; text-align: center;
  }
  .card--front { left: 70px; top: 110px; padding-top: 46px; }
  .card--back  { left: 590px; top: 470px; justify-content: center; }

  .brand { display: flex; flex-direction: column; align-items: center; }
  .brand__square {
    width: 22px; height: 22px; background: var(--ink-mid); margin-bottom: 14px;
  }
  .brand__name {
    font-weight: 600; font-size: 15px; letter-spacing: 1.5px;
    color: var(--ink-light); text-transform: uppercase; white-space: nowrap;
  }
  .card--back .brand__square { width: 34px; height: 34px; margin-bottom: 22px; }
  .card--back .brand__name { font-size: 26px; letter-spacing: 3px; color: var(--ink-mid); font-weight: 400; }

  .agents { margin-top: 34px; font-size: 22px; letter-spacing: .5px; white-space: nowrap; }
  .role { margin-top: 4px; font-size: 12px; letter-spacing: 1px; color: var(--ink-mid); }
  .contact { margin-top: 30px; font-size: 12px; letter-spacing: .6px; line-height: 1.8; white-space: nowrap; }
</style>
</head>
<body>
<main class="stage">
  <section class="card card--front" aria-label="Business card front">
    <div class="brand">
      <span class="brand__square"></span>
      <span class="brand__name">Walsh &amp; Brody Pty Ltd.</span>
    </div>
    <p class="agents">Paul Walsh &amp; Lucy Brody</p>
    <p class="role">Sales Agents &amp; Onsite Manager</p>
    <div class="contact">
      <p>P 07 5948 2063 &nbsp;: F 07 5948 2174 &nbsp;: M 0461 857 239</p>
      <p>A: 3/42 Marlin Crescent, ASHFORD VALE QLD 4190</p>
    </div>
  </section>

  <section class="card card--back" aria-label="Business card back">
    <div class="brand">
      <span class="brand__square"></span>
      <span class="brand__name">Walsh &amp; Brody Pty Ltd.</span>
    </div>
  </section>
</main>
</body>
</html>
```